Awesome photographers card for an awesome new business

Double sided business card Black background and silver logo in middle on one side. Details on otherside. please keep it simple

Photographer

Gavin Tolley
0482615073
GavinTolleyPhotography82@lumenpost.com
www.GavinTolleyPhotography.com.au
Instagram _Gavin_tolley

Requirements
Must have
• My logo in Silver
• please use instagram logo instead of "Instagram"

```html
<!DOCTYPE html>
<html lang="en">
<head>
<meta charset="utf-8">
<title>Gavin Tolley Photography – Business Card</title>
<link rel="stylesheet" href="https://fonts.googleapis.com/css2?family=Open+Sans:wght@400;700&display=swap">
<style>
  :root {
    --backdrop: #3a3430;
    --card: #0c0c0c;
    --card-edge: #1a1a1a;
    --silver: #d9d9d9;
    --silver-dim: #9a9a9a;
    --divider: #2c2c2c;
  }
  * { box-sizing: border-box; margin: 0; padding: 0; }
  html, body { width: 1200px; height: 900px; overflow: hidden; }
  body {
    background: var(--backdrop);
    font-family: "Open Sans", Arial, sans-serif;
    position: relative;
  }
  .card {
    position: absolute;
    top: 290px;
    width: 540px;
    height: 320px;
    background: var(--card);
    border: 1px solid var(--card-edge);
    box-shadow: 0 14px 30px rgba(0,0,0,.45);
  }
  .card--details { left: 40px; }
  .card--brand { left: 620px; display: flex; align-items: center; justify-content: center; }

  .brand-mark {
    display: flex;
    align-items: center;
    gap: 12px;
    color: var(--silver);
    font-weight: 400;
    font-size: 17px;
    letter-spacing: 1px;
    text-transform: uppercase;
  }
  .brand-mark__dot {
    width: 16px; height: 16px;
    border: 2px solid var(--silver);
    border-radius: 50%;
    flex: none;
  }
  .brand-mark__name { line-height: 1.35; text-align: left; }

  .details-logo {
    position: absolute;
    left: 0; top: 0;
    width: 210px; height: 100%;
    display: flex; align-items: center; justify-content: center;
    border-right: 1px solid var(--divider);
  }
  .details-logo .brand-mark { font-size: 13px; gap: 9px; }
  .details-logo .brand-mark__dot { width: 12px; height: 12px; }

  .contact {
    position: absolute;
    left: 238px; top: 92px;
    color: var(--silver);
  }
  .contact__name {
    font-weight: 700;
    font-size: 17px;
    margin-bottom: 18px;
  }
  .contact__list { list-style: none; }
  .contact__item {
    display: flex; align-items: center; gap: 10px;
    font-size: 12.5px;
    line-height: 23px;
    color: var(--silver);
  }
  .contact__icon { width: 11px; height: 11px; flex: none; fill: var(--silver-dim); stroke: var(--silver-dim); }
</style>
</head>
<body>
  <section class="card card--details" aria-label="Business card, contact side">
    <div class="details-logo">
      <div class="brand-mark">
        <span class="brand-mark__dot"></span>
        <span class="brand-mark__name">Gavin Tolley<br>Photography</span>
      </div>
    </div>
    <div class="contact">
      <h1 class="contact__name">Gavin Tolley</h1>
      <ul class="contact__list">
        <li class="contact__item">
          <svg class="contact__icon" viewBox="0 0 12 12" aria-hidden="true"><path stroke="none" d="M2.5 0.5l2 2-1 1.5c.6 1.6 1.9 2.9 3.5 3.5l1.5-1 2 2-1.3 1.8C5 10 2 7 0.7 1.8z"/></svg>
          0482615073
        </li>
        <li class="contact__item">
          <svg class="contact__icon" viewBox="0 0 12 12" aria-hidden="true"><rect x="0.5" y="2" width="11" height="8" fill="none" stroke-width="1.2"/><path d="M0.5 2l5.5 4.5L11.5 2" fill="none" stroke-width="1.2"/></svg>
          GavinTolleyPhotography82@lumenpost.com
        </li>
        <li class="contact__item">
          <svg class="contact__icon" viewBox="0 0 12 12" aria-hidden="true"><circle cx="6" cy="6" r="5" fill="none" stroke-width="1.2"/><path d="M1 6h10M6 1c2.5 2.8 2.5 7.2 0 10M6 1c-2.5 2.8-2.5 7.2 0 10" fill="none" stroke-width="1"/></svg>
          www.GavinTolleyPhotography.com.au
        </li>
        <li class="contact__item">
          <svg class="contact__icon" viewBox="0 0 12 12" aria-hidden="true"><rect x="1" y="1" width="10" height="10" fill="none" stroke-width="1.4"/></svg>
          Gavin_tolley
        </li>
      </ul>
    </div>
  </section>

  <section class="card card--brand" aria-label="Business card, logo side">
    <div class="brand-mark">
      <span class="brand-mark__dot"></span>
      <span class="brand-mark__name">Gavin Tolley<br>Photography</span>
    </div>
  </section>
</body>
</html>
```